KVO-Business Card Design

I need a modern, professional business card design that includes my logo as the main feature, maybe the entire background with the contact info overlaying or even contact info on the back and the logo full frontal

Neat and organized placement of contact information

Would like to see options in black and white

Target Market(s)

real estate Developers, Construction managers, business and home owners

Industry/Entity Type

Construction

Contact Information for Business Card

KVO Construction
Danny Ferrante
General Contractor

Office: 1-888-902-7315 Ext #1
Cell: 215-730-4162
Fax: 1-888-902-7315

Font styles to use
Serif

Requirements
Must have
• title
• office #
• cell #
• Email
• website
Nice to have
• fax

```html
<!DOCTYPE html>
<html lang="en">
<head>
<meta charset="utf-8">
<title>KVO Construction – Business Card</title>
<link href="https://fonts.googleapis.com/css2?family=Roboto:wght@400;700;900&display=swap" rel="stylesheet">
<style>
  :root {
    --backdrop: #265c3e;
    --card: #000000;
    --brand-green: #1fa84f;
    --text-light: #f2f2f2;
    --ghost: #0c2416;
  }
  * { margin: 0; padding: 0; box-sizing: border-box; }
  html, body { width: 1200px; height: 900px; overflow: hidden; }
  body {
    background: var(--backdrop);
    font-family: "Roboto", Arial, sans-serif;
    position: relative;
  }
  .card {
    position: absolute;
    width: 520px;
    height: 296px;
    background: var(--card);
    border-radius: 3px;
    box-shadow: 0 14px 30px rgba(0,0,0,.35);
    overflow: hidden;
  }
  .card--front { left: 70px; top: 110px; }
  .card--back { left: 610px; top: 494px; }

  .brand-mark {
    display: flex;
    align-items: center;
    gap: 14px;
    color: var(--brand-green);
    font-weight: 900;
  }
  .brand-mark__square {
    background: var(--brand-green);
    flex: none;
  }
  .card--front .brand-mark {
    position: absolute;
    left: 0; right: 0; top: 0; bottom: 0;
    justify-content: center;
    font-size: 46px;
    letter-spacing: 1px;
  }
  .card--front .brand-mark__square { width: 28px; height: 28px; }

  .card--back .brand-mark {
    position: absolute;
    right: 26px;
    top: 30px;
    font-size: 20px;
    gap: 8px;
  }
  .card--back .brand-mark__square { width: 14px; height: 14px; }

  .ghost-name {
    position: absolute;
    right: -10px;
    bottom: 40px;
    font-weight: 900;
    font-size: 130px;
    color: var(--ghost);
    line-height: 1;
  }

  .contact {
    position: absolute;
    left: 30px;
    bottom: 30px;
    color: var(--text-light);
  }
  .contact__name {
    color: var(--brand-green);
    font-weight: 900;
    font-size: 21px;
    letter-spacing: .5px;
    text-transform: uppercase;
  }
  .contact__title {
    font-size: 11px;
    letter-spacing: 1px;
    margin-bottom: 18px;
  }
  .contact__list {
    display: grid;
    grid-template-columns: 54px auto;
    font-size: 12.5px;
    letter-spacing: 1px;
    line-height: 1.45;
  }
  .contact__email { grid-column: 1 / 3; }
  .contact__web {
    margin-top: 16px;
    color: var(--brand-green);
    font-size: 12.5px;
    font-weight: 700;
    letter-spacing: 1.5px;
  }
</style>
</head>
<body>
  <section class="card card--front" aria-label="Business card front">
    <div class="brand-mark">
      <span class="brand-mark__square"></span>
      <span class="brand-mark__name">KVO Construction</span>
    </div>
  </section>

  <section class="card card--back" aria-label="Business card back">
    <div class="ghost-name" aria-hidden="true">KVO</div>
    <div class="brand-mark">
      <span class="brand-mark__square"></span>
      <span class="brand-mark__name">KVO Construction</span>
    </div>
    <div class="contact">
      <p class="contact__name">Danny Ferrante</p>
      <p class="contact__title">General Contractor</p>
      <div class="contact__list">
        <span>Office</span><span>1-888-902-7315 Ext #1</span>
        <span>Cell</span><span>215-730-4162</span>
        <span>Fax</span><span>1-888-902-7315</span>
        <span class="contact__email">danny@KVOConstruction.com</span>
      </div>
      <p class="contact__web">www.KVOConstruction.com</p>
    </div>
  </section>
</body>
</html>
```